QSL Card

project is a QSL card for amateur radio operators - must radio show call sign predomiately and in large letters on the card - VK5RUT - then must say somewhere Greetings from Australia - must also include name, address, website and coordinates in small trype - Martin Keble,47 Birch Rd., Tarrowby SA 5170 Australia, http://www.martinkebleqsl.com, - Grid Square PF82kr, CQ Zone 30, ITU Zone 59 - must also have a long rectangular box down the bottom of the card with six boxes inside the long box that can be filled in showing a heading in each box --- in box 1 Confirming QSO with.... box 2 Date (Z) ....., box 3 UTC ...... box 4 Freq / 2XMode ...... box 5 Pwr Out,..... boxx 6 Report ..... use attached pictures in the design with the radio equiipment as a background and my photo superimposed somewhere -- and the other attached image shows how i want the box to look - and on the right hand side down the bottom in small letters - 73s, Tnx QSL Pse

Reason: none of the designs i received totally fit the bill - see my new brief and budget

hi all - i finally decided i didnt like any of the designs i received so i have increased the budget and extended the deadline - i have also updated my brief and added another picture

Target Market(s)

amateur radio operators

Industry/Entity Type

Radio

Colors

Designer to choose colors to be used in the design.

```html
<!DOCTYPE html>
<html lang="en">
<head>
<meta charset="utf-8">
<title>VK5RUT QSL Card – Martin Keble</title>
<link rel="stylesheet" href="https://fonts.googleapis.com/css2?family=Raleway:wght@500;600;700;800&family=Open+Sans:wght@400;600;700&display=swap">
<style>
  :root {
    --page-bg: #e9e7e3;
    --card-navy: #14223a;
    --card-navy-deep: #0b1526;
    --header-navy: #1b2c4a;
    --panel-navy: rgba(20, 34, 58, 0.8);
    --photo-light: #8d9cae;
    --photo-mid: #5b6b80;
    --photo-dark: #2e3b4f;
    --text-white: #ffffff;
    --text-soft: #d5dbe5;
    --rule: rgba(255, 255, 255, 0.55);
    --box-line: rgba(255, 255, 255, 0.7);
  }
  * { box-sizing: border-box; margin: 0; padding: 0; }
  html, body {
    width: 851px; height: 1200px; overflow: hidden;
    background: var(--page-bg);
  }
  .qsl-card {
    position: absolute;
    left: 30px; top: 250px;
    width: 791px; height: 700px;
    background: linear-gradient(180deg, var(--card-navy) 0%, var(--card-navy-deep) 100%);
    color: var(--text-white);
    font-family: "Open Sans", sans-serif;
    box-shadow: 0 6px 18px rgba(0,0,0,0.25);
    overflow: hidden;
  }
  .card-header {
    height: 100px;
    display: flex; align-items: baseline; justify-content: center; gap: 22px;
    padding-top: 14px;
    background: var(--header-navy);
  }
  .call-sign {
    font-family: "Raleway", sans-serif;
    font-weight: 800;
    font-size: 64px;
    letter-spacing: 2px;
    line-height: 1;
  }
  .operator-name {
    font-family: "Raleway", sans-serif;
    font-weight: 700;
    font-size: 28px;
    font-variant: small-caps;
    color: var(--text-soft);
  }
  .photo-band { position: relative; height: 250px; }
  .station-photo {
    position: absolute; inset: 0;
    background: linear-gradient(100deg, var(--photo-dark) 0%, var(--photo-mid) 30%, var(--photo-light) 55%, var(--photo-mid) 80%, var(--photo-dark) 100%);
  }
  .greeting {
    position: absolute; left: 22px; bottom: 16px;
    font-family: "Raleway", sans-serif;
    font-weight: 700; font-size: 24px;
    color: var(--text-white);
    background: var(--panel-navy);
    padding: 4px 12px;
  }
  .log-panel {
    position: absolute; right: 0; top: 0; bottom: 0;
    width: 370px;
    background: var(--panel-navy);
    padding: 12px 20px 0 30px;
  }
  .log-list { list-style: none; }
  .log-list li {
    font-family: "Raleway", sans-serif;
    font-weight: 600; font-size: 25px; line-height: 37px;
  }
  .log-list li:nth-child(2) { padding-left: 22px; }
  .log-list li:nth-child(3) { padding-left: 44px; }
  .log-list li:nth-child(4) { padding-left: 22px; }
  .log-list li:nth-child(5) { padding-left: 44px; }
  .log-list li:nth-child(6) { padding-left: 66px; }
  .qso-box {
    display: grid;
    grid-template-columns: 1.7fr 1fr 0.8fr 1.3fr 0.9fr 0.9fr;
    margin: 14px 24px 0;
    height: 74px;
    border: 2px solid var(--box-line);
  }
  .qso-field {
    border-left: 1px solid var(--box-line);
    padding: 5px 7px;
    font-size: 12px; font-weight: 600;
    color: var(--text-soft);
  }
  .qso-field:first-child { border-left: none; }
  .contact-rule { height: 2px; margin: 14px 24px 0; background: var(--rule); }
  .contact-block { padding: 8px 34px 0; position: relative; height: 230px; }
  .call-line {
    display: flex; align-items: center; justify-content: center; gap: 14px;
    font-family: "Raleway", sans-serif;
    font-weight: 700; font-size: 34px;
  }
  .call-line svg { width: 30px; height: 30px; }
  .detail-line {
    display: flex; align-items: center; gap: 10px;
    font-size: 20px; color: var(--text-soft);
    margin-top: 10px;
  }
  .detail-line svg { width: 21px; height: 21px; flex: none; }
  .grid-line {
    font-size: 15px; color: var(--text-soft);
    margin-top: 12px; letter-spacing: 0.3px;
  }
  .sign-off {
    position: absolute; right: 24px; bottom: 40px;
    font-size: 12px; color: var(--text-soft);
  }
</style>
</head>
<body>
  <main class="qsl-card">
    <header class="card-header">
      <h1 class="call-sign">VK5RUT</h1>
      <p class="operator-name">Martin Keble</p>
    </header>

    <section class="photo-band">
      <div class="station-photo" role="img" aria-label="Operator seated at his amateur radio station with transceivers and monitor"></div>
      <p class="greeting">Greetings from Australia</p>
      <div class="log-panel">
        <ol class="log-list">
          <li>1/ Confirming QSO with</li>
          <li>2/ date (Z),</li>
          <li>3/ UTC</li>
          <li>4/ Freq / 2XMode</li>
          <li>5/ pwr Out,</li>
          <li>6/ Report</li>
        </ol>
      </div>
    </section>

    <section class="qso-box" aria-label="Contact details to fill in">
      <div class="qso-field">Confirming QSO with</div>
      <div class="qso-field">Date (Z)</div>
      <div class="qso-field">UTC</div>
      <div class="qso-field">Freq / 2XMode</div>
      <div class="qso-field">Pwr Out</div>
      <div class="qso-field">Report</div>
    </section>

    <div class="contact-rule"></div>

    <section class="contact-block">
      <p class="call-line">
        Call NOW
        <svg viewBox="0 0 32 32" aria-hidden="true">
          <circle cx="16" cy="16" r="14" fill="none" stroke="#fff" stroke-width="2"/>
          <path d="M11 9c1-1 2-1 3 0l1.5 2.5c.5 1 .3 1.8-.5 2.4l-1 .8c.8 2 2.3 3.5 4.3 4.3l.8-1c.6-.8 1.4-1 2.4-.5L24 19c1 1 1 2 0 3l-1 1c-5 0-13-8-13-13z" fill="#fff"/>
        </svg>
        08 8471-2093
      </p>
      <p class="detail-line">
        <svg viewBox="0 0 24 24" aria-hidden="true">
          <path d="M12 2a7 7 0 0 0-7 7c0 5 7 13 7 13s7-8 7-13a7 7 0 0 0-7-7zm0 9.5A2.5 2.5 0 1 1 12 6.5a2.5 2.5 0 0 1 0 5z" fill="#fff"/>
        </svg>
        47 Birch Rd., Tarrowby SA 5170 Australia
      </p>
      <p class="detail-line">
        <svg viewBox="0 0 24 24" aria-hidden="true">
          <circle cx="12" cy="12" r="9.5" fill="none" stroke="#fff" stroke-width="1.8"/>
          <ellipse cx="12" cy="12" rx="4" ry="9.5" fill="none" stroke="#fff" stroke-width="1.5"/>
          <path d="M2.5 12h19M4 7h16M4 17h16" stroke="#fff" stroke-width="1.3"/>
        </svg>
        www.martinkebleqsl.com
      </p>
      <p class="grid-line">Grid Square PF82kr &nbsp;·&nbsp; CQ Zone 30 &nbsp;·&nbsp; ITU Zone 59</p>
      <p class="sign-off">73s, Tnx QSL Pse</p>
    </section>
  </main>
</body>
</html>
```